Harlow Stonefield Civil Construction website design

We want a Bold website to promote our Heavy Civil Construction company, We would like an organic / tangible feel to the site. The pictures will be over saturated so they pop. We need to be able to easliy upload new projects and pictures on a regular basis.
Home page will have a full screen width image, "home page image" with silhouette and logo. It will also have about us area and picture
Page 2 will be Project Gallery with pictures in project folders
Page 3 will be an employment application form and submission
Page 4 will be Contact Us
Target Market(s)
Construction indusrty
Industry/Entity Type
Contractor
Coding
Coded - Design and coding required
Number of Pages Required
4 page
Font styles to use
Other font styles liked:
- Hypatia Sans Pro Light
Look and feel

```html
<!DOCTYPE html>
<html lang="en">
<head>
<meta charset="utf-8">
<title>Harlow Stonefield Civil Construction – Gallery</title>
<link href="https://fonts.googleapis.com/css2?family=Poppins:wght@400;500;600;700&display=swap" rel="stylesheet">
<style>
  :root {
    --ink: #000000;
    --white: #ffffff;
    --brand: #3a56a8;
    --brand-soft: #4b63b8;
    --grey-title: #6f6f6f;
    --grey-line: #cfcfcf;
    --grey-text: #9a9a9a;
    --footer: #0d0d0d;
    --crumb-muted: #d6dde8;
  }
  * { box-sizing: border-box; margin: 0; padding: 0; }
  html, body { width: 869px; height: 1200px; overflow: hidden; background: var(--white); }
  body { position: relative; font-family: "Poppins", sans-serif; color: var(--ink); }
  .abs { position: absolute; }

  .hero {
    left: 0; top: 0; width: 869px; height: 205px;
    background:
      linear-gradient(90deg, rgba(0,0,0,.45) 0%, rgba(0,0,0,.15) 45%, rgba(0,0,0,0) 70%),
      linear-gradient(160deg, #1f5a55 0%, #2f5c58 30%, #4d5a58 60%, #6e7072 100%);
  }
  .nav-bar { left: 0; top: 18px; width: 728px; height: 60px; background: var(--ink); }
  .brand { display: flex; align-items: center; gap: 8px; }
  .brand-mark { width: 26px; height: 26px; background: var(--brand); flex: none; }
  .brand-name { color: var(--white); font-weight: 500; font-size: 11px; line-height: 1.25; text-transform: uppercase; letter-spacing: .6px; }
  .nav-brand { left: 50px; top: 34px; }
  .nav-link { top: 39px; color: var(--white); font-size: 11px; font-weight: 600; }
  .nav-link.active { color: var(--brand-soft); }
  .hero-title { left: 63px; top: 100px; color: var(--white); font-size: 37px; font-weight: 600; letter-spacing: 1px; }
  .crumbs { left: 61px; top: 151px; color: var(--white); font-size: 14px; font-weight: 600; }
  .crumbs .home { color: var(--crumb-muted); font-weight: 400; }

  .bar { height: 5px; background: var(--brand); }
  .section-title { left: 0; width: 821px; top: 254px; text-align: center; color: var(--grey-title); font-size: 38px; font-weight: 600; letter-spacing: 1px; }

  .filter { top: 361px; height: 27px; border: 2px solid var(--grey-line); color: var(--grey-text); font-size: 12px; display: flex; align-items: center; justify-content: center; letter-spacing: .4px; }
  .filter.active { background: var(--brand); border-color: var(--brand); color: var(--white); font-weight: 500; }

  .tile { width: 240px; height: 220px; }
  .tile-overlay { background: rgba(255,255,255,.55); }

  .footer { left: 0; top: 918px; width: 869px; height: 282px; background: radial-gradient(circle at 40% 30%, #1b1b1b, var(--footer) 70%); }
  .foot-brand { left: 60px; top: 966px; }
  .foot-brand .brand-mark { width: 30px; height: 30px; }
  .foot-brand .brand-name { font-size: 12px; }
  .foot-about { left: 58px; top: 1013px; width: 250px; color: var(--white); font-size: 10px; line-height: 14px; }
  .foot-head { top: 963px; color: var(--white); font-size: 16px; font-weight: 600; }
  .foot-rule { top: 993px; width: 36px; height: 2px; background: var(--brand); }
  .foot-link { left: 347px; color: var(--white); font-size: 10px; }
  .foot-link.active { color: var(--brand-soft); }
  .news-text { left: 500px; top: 1012px; width: 156px; color: var(--white); font-size: 9px; line-height: 17px; text-align: justify; }
  .news-input { left: 501px; top: 1084px; width: 150px; height: 24px; background: var(--white); font-size: 7.5px; color: #333; padding: 7px 10px; }
  .news-btn { left: 501px; top: 1131px; width: 77px; height: 26px; border-radius: 13px; background: var(--brand); color: var(--white); font-size: 8.5px; font-weight: 700; display: flex; align-items: center; justify-content: center; }
  .thumb { width: 42px; height: 39px; }
</style>
</head>
<body>
  <header>
    <div class="abs hero" role="img" aria-label="Worker hosing down a rock-filled gabion wall beside water"></div>
    <div class="abs nav-bar"></div>
    <div class="abs brand nav-brand"><span class="brand-mark"></span><span class="brand-name">Harlow Stonefield<br>Civil Construction</span></div>
    <nav>
      <span class="abs nav-link" style="left:422px">HOME</span>
      <span class="abs nav-link" style="left:478px">ABOUT US</span>
      <span class="abs nav-link" style="left:555px">CONTACT US</span>
      <span class="abs nav-link active" style="left:645px">GALLERY</span>
    </nav>
    <h1 class="abs hero-title">Gallery</h1>
    <div class="abs crumbs"><span class="home">Home</span> &gt;&gt; Gallery</div>
  </header>

  <main>
    <div class="abs bar" style="left:342px;top:248px;width:48px"></div>
    <h2 class="abs section-title">Gallery</h2>
    <div class="abs bar" style="left:445px;top:313px;width:49px"></div>

    <div class="abs filter active" style="left:174px;width:102px">All Projects</div>
    <div class="abs filter" style="left:280px;width:78px">Houses</div>
    <div class="abs filter" style="left:363px;width:97px">Consultant</div>
    <div class="abs filter" style="left:464px;width:74px">Interior</div>
    <div class="abs filter" style="left:542px;width:89px">Designs</div>

    <div class="abs tile" style="left:63px;top:418px;background:linear-gradient(180deg,#6f8f5e 0%,#8fa184 35%,#b9bfb8 55%,#8a98a0 100%)" role="img" aria-label="Drainage canal lined with sandbag wall"></div>
    <div class="abs tile tile-overlay" style="left:63px;top:418px"></div>
    <svg class="abs" style="left:153px;top:502px" width="58" height="58" viewBox="0 0 58 58"><path d="M29 0V58M0 29H58" stroke="#333" stroke-width="2"/></svg>
    <div class="abs tile" style="left:322px;top:418px;background:linear-gradient(180deg,#3f8fe0 0%,#7fb6ea 35%,#d9733a 62%,#7a4a2c 100%)" role="img" aria-label="Orange excavator digging at a site"></div>
    <div class="abs tile" style="left:581px;top:418px;background:linear-gradient(180deg,#a9cde0 0%,#b8c9c2 40%,#4d6b3e 55%,#8d7b6e 75%,#6b5a50 100%)" role="img" aria-label="Earthworks with dirt mounds and trench"></div>
    <div class="abs tile" style="left:63px;top:656px;background:linear-gradient(180deg,#a8c4e4 0%,#d3d8dc 30%,#9a6a3c 60%,#5b3d28 100%)" role="img" aria-label="Crew installing trench shoring box"></div>
    <div class="abs tile" style="left:322px;top:656px;background:linear-gradient(120deg,#3e7a3a 0%,#1f5fa0 35%,#6b8f4d 55%,#8d8f90 80%,#b3b1a6 100%)" role="img" aria-label="Aerial view of highway beside a pond"></div>
    <div class="abs tile" style="left:581px;top:656px;background:linear-gradient(180deg,#5e8f4c 0%,#c9b87a 35%,#6a5a3c 60%,#a9a196 100%)" role="img" aria-label="Loader dumping gravel at a work site"></div>
  </main>

  <footer>
    <div class="abs footer"></div>
    <div class="abs brand foot-brand"><span class="brand-mark"></span><span class="brand-name">Harlow Stonefield<br>Civil Construction</span></div>
    <p class="abs foot-about">Lorem ipsum dolor sit amet, consectetur quam justo, pretium adipiscing elit. Vestibulum quam justo, pretium eu tempus ut, ..</p>

    <h3 class="abs foot-head" style="left:343px">QUICK LINK</h3>
    <div class="abs foot-rule" style="left:347px"></div>
    <span class="abs foot-link" style="top:1015px">Home</span>
    <span class="abs foot-link" style="top:1054px">About us</span>
    <span class="abs foot-link" style="top:1093px">Contact us</span>
    <span class="abs foot-link active" style="top:1131px">Gallery</span>

    <h3 class="abs foot-head" style="left:497px">NEWSLETTER</h3>
    <div class="abs foot-rule" style="left:499px"></div>
    <p class="abs news-text">Subscribe to this website and receive notifications of new posts by email.</p>
    <div class="abs news-input">Email Address</div>
    <div class="abs news-btn">SUBSCRIBE</div>

    <h3 class="abs foot-head" style="left:725px">GALLERY</h3>
    <div class="abs foot-rule" style="left:727px"></div>
    <div class="abs thumb" style="left:726px;top:1018px;background:linear-gradient(180deg,#8aa9c9,#777c7a)" role="img" aria-label="Road project thumbnail"></div>
    <div class="abs thumb" style="left:776px;top:1018px;background:linear-gradient(180deg,#9cc3e0,#c08a3a 60%,#5b6b3c)" role="img" aria-label="Excavator thumbnail"></div>
    <div class="abs thumb" style="left:726px;top:1065px;background:linear-gradient(180deg,#a9b9c8,#5c6570)" role="img" aria-label="Steel structure thumbnail"></div>
    <div class="abs thumb" style="left:776px;top:1065px;background:linear-gradient(180deg,#2f6fc0,#b36a3c 65%,#7a4a30)" role="img" aria-label="Site at dusk thumbnail"></div>
  </footer>
</body>
</html>
```